Global Weight loss program

we need a business card based in Brooklyn , NY called PeppertonRUN . Mara Dulvik Tenbrook the founder and creator of PeppertonRUN Movement. A business based around nutrition, health, Whole Foods and fitness.

Industry/Entity Type

Food Service

Contact Information for Business Card

Phone number : 718-555-0143
website www.peppertonrun.com
email : mara@peppertonrun.com

Font styles to use
Sans Serif

Requirements
Must have
• logo colors
• green black and gold
Nice to have
• must be simple and sharp.
Should not have
• pictures of items

```html
<!DOCTYPE html>
<html lang="en">
<head>
<meta charset="utf-8">
<title>PeppertonRUN Business Card</title>
<link rel="stylesheet" href="https://fonts.googleapis.com/css2?family=Open+Sans:wght@400;600;700&display=swap">
<style>
  :root {
    --green: #6cb33f;
    --green-light: #8cc63f;
    --green-dark: #4f9a2a;
    --ink: #333333;
    --grey: #777777;
    --paper: #ffffff;
    --backdrop: #ece9e3;
  }
  * { margin: 0; padding: 0; box-sizing: border-box; }
  html, body { width: 1200px; height: 1023px; overflow: hidden; }
  body {
    background: var(--backdrop);
    font-family: "Open Sans", Arial, sans-serif;
    position: relative;
  }
  .card {
    position: absolute;
    width: 700px;
    height: 400px;
    border-radius: 18px;
    overflow: hidden;
    box-shadow: 0 10px 28px rgba(0,0,0,0.18);
  }
  /* Front */
  .card-front { left: 40px; top: 60px; background: linear-gradient(180deg, #ffffff, #f1f1f1); }
  .front-figure {
    position: absolute; left: 330px; top: 20px; width: 200px; height: 200px;
    background: radial-gradient(ellipse at center, rgba(140,198,63,0.10), rgba(140,198,63,0) 70%);
  }
  .front-rule {
    position: absolute; left: 40px; right: 40px; top: 222px; height: 1px;
    background: var(--green-light);
  }
  .front-name {
    position: absolute; right: 40px; top: 180px;
    font-weight: 700; font-size: 30px; letter-spacing: 3px; color: var(--green);
  }
  .brand { position: absolute; left: 40px; top: 118px; display: flex; align-items: center; gap: 14px; }
  .brand-mark { width: 50px; height: 50px; background: var(--green); flex: none; }
  .brand-name {
    font-size: 32px; font-weight: 600; color: var(--ink);
    line-height: 1; letter-spacing: 2px; text-transform: uppercase;
  }
  .brand-tag { font-size: 12px; color: var(--grey); letter-spacing: 2px; margin-top: 8px; }
  .contacts { position: absolute; left: 40px; top: 244px; list-style: none; }
  .contacts li {
    display: flex; align-items: center; gap: 10px;
    font-size: 17px; color: var(--ink); line-height: 1.75;
  }
  .contacts svg { width: 16px; height: 16px; flex: none; }
  .address {
    position: absolute; right: 40px; top: 254px; text-align: right;
    font-size: 16px; color: var(--ink); line-height: 1.4;
    display: flex; gap: 10px; align-items: flex-start;
  }
  .address svg { width: 16px; height: 20px; flex: none; margin-top: 2px; }
  .front-band {
    position: absolute; left: 0; right: 0; bottom: 0; height: 48px;
    background: linear-gradient(180deg, var(--green-light), var(--green));
  }
  /* Back */
  .card-back {
    left: 460px; top: 560px;
    background: radial-gradient(ellipse at 55% 50%, var(--green-light), var(--green-dark));
    display: flex; align-items: center; justify-content: center; gap: 28px;
    color: var(--paper);
  }
  .back-mark { width: 96px; height: 96px; background: var(--paper); flex: none; }
  .back-name {
    font-size: 46px; font-weight: 600; letter-spacing: 3px;
    line-height: 1; text-transform: uppercase;
  }
  .back-tag { font-size: 15px; letter-spacing: 3px; margin-top: 12px; }
</style>
</head>
<body>
  <section class="card card-front" aria-label="Business card front">
    <div class="front-figure" role="img" aria-label="Faint silhouette of a runner"></div>
    <div class="brand">
      <div class="brand-mark"></div>
      <div>
        <div class="brand-name">PeppertonRUN</div>
        <div class="brand-tag">Fitness, Nutrition and Health</div>
      </div>
    </div>
    <div class="front-rule"></div>
    <div class="front-name">Your Name</div>
    <ul class="contacts">
      <li>
        <svg viewBox="0 0 16 16"><circle cx="8" cy="8" r="7.5" fill="var(--green-light)"/><path d="M5 4.5c0 4 2.5 6.5 6.5 7l1-1.6-1.8-1-0.9 0.9c-1.2-0.5-2.1-1.4-2.6-2.6l0.9-0.9-1-1.8z" fill="#fff"/></svg>
        718-555-0143
      </li>
      <li>
        <svg viewBox="0 0 16 16"><rect x="1" y="3.5" width="14" height="9" rx="1" fill="var(--green-light)"/><path d="M1.5 4l6.5 5 6.5-5" stroke="#fff" stroke-width="1.2" fill="none"/></svg>
        mara@peppertonrun.com
      </li>
      <li>
        <svg viewBox="0 0 16 16"><circle cx="8" cy="8" r="7.5" fill="var(--green-light)"/><path d="M2 8h12M8 1v14M8 1c-3 3-3 11 0 14M8 1c3 3 3 11 0 14" stroke="#fff" stroke-width="1" fill="none"/></svg>
        www.peppertonrun.com
      </li>
    </ul>
    <div class="address">
      <div>Your Address is<br>here in just two line</div>
      <svg viewBox="0 0 16 20"><path d="M8 0a7 7 0 0 0-7 7c0 5 7 13 7 13s7-8 7-13a7 7 0 0 0-7-7z" fill="var(--green)"/><circle cx="8" cy="7" r="2.6" fill="#fff"/></svg>
    </div>
    <div class="front-band"></div>
  </section>

  <section class="card card-back" aria-label="Business card back">
    <div class="back-mark"></div>
    <div>
      <div class="back-name">PeppertonRUN</div>
      <div class="back-tag">Fitness, Nutrition and Health</div>
    </div>
  </section>
</body>
</html>
```